Ninety Truths Earned Across Four Decades of Advisory Work

I need the design for my book cover, plus the spine and the back cover. I need this for both a hard cover book and an ebook

Target Market(s)

Any person in business with managerial responsibility

Industry/Entity Type

Consulting

Font styles to use
Serif

Requirements
Must have
• Must look very professional. No script/cursive is to be used. The cover should be clean, not cluttered.so the title really stands out well
Nice to have
• A professional image to reinforce the title
Should not have
• Script, cartoons or anything that does not look professional

```html
<!DOCTYPE html>
<html lang="en">
<head>
<meta charset="utf-8">
<title>Ninety Truths Earned Across Four Decades of Advisory Work – Cover Wrap</title>
<link href="https://fonts.googleapis.com/css2?family=Lato:wght@300;400;700;900&display=swap" rel="stylesheet">
<style>
  :root {
    --red: #c63135;
    --white: #ffffff;
    --ink: #0b0b0b;
    --backdrop: #ececec;
  }
  * { margin: 0; padding: 0; box-sizing: border-box; }
  html, body { width: 870px; height: 1200px; overflow: hidden; }
  body {
    background: var(--backdrop);
    font-family: "Lato", Arial, sans-serif;
    position: relative;
  }
  .cover-wrap {
    position: absolute;
    left: 0; top: 289px;
    width: 870px; height: 622px;
    display: flex;
  }

  /* Back cover */
  .back-cover { width: 415px; height: 100%; display: flex; flex-direction: column; }
  .back-cover .top-band {
    height: 99px; background: var(--white);
    display: flex; align-items: center; justify-content: center;
  }
  .back-cover .author {
    color: var(--red); font-weight: 700; font-size: 31px; letter-spacing: -0.3px;
  }
  .back-cover .blurb-band {
    height: 424px; background: var(--red);
    padding: 23px 39px 0 39px;
  }
  .blurb {
    color: var(--ink); font-size: 16.6px; line-height: 21.4px;
    text-align: justify; text-align-last: center; text-indent: 25px;
  }
  .back-cover .bottom-band { flex: 1; background: var(--white); }

  /* Spine */
  .spine {
    width: 40px; height: 100%; background: var(--red);
    position: relative;
  }
  .spine .author {
    position: absolute; top: 36px; left: 50%;
    transform: translateX(-50%);
    writing-mode: vertical-rl;
    color: var(--white); font-weight: 700; font-size: 25px; line-height: 1;
  }
  .spine .title {
    position: absolute; top: 310px; left: 3px;
    writing-mode: vertical-rl;
    color: var(--white); font-size: 12.6px; line-height: 17px; font-weight: 300;
    white-space: nowrap;
  }
  .spine .title b { font-weight: 900; }

  /* Front cover */
  .front-cover { width: 415px; height: 100%; display: flex; flex-direction: column; }
  .front-cover .top-band { height: 99px; background: var(--red); }
  .front-cover .title-band {
    height: 424px; background: var(--white); position: relative;
  }
  .front-cover .bottom-band {
    flex: 1; background: var(--red);
    display: flex; align-items: center; justify-content: center;
  }
  .front-cover .author { color: var(--white); font-weight: 700; font-size: 31px; }

  .title-block {
    position: absolute; left: 44px; top: 84px; width: 330px;
    color: var(--red);
  }
  .title-row { display: flex; align-items: baseline; justify-content: space-between; }
  .light-word { font-weight: 300; line-height: 1; }
  .bold-word { font-weight: 900; line-height: 1; }
  .row-1 .light-word { font-size: 60px; }
  .row-1 .bold-word { font-size: 40px; }
  .subline {
    text-align: right; color: var(--ink); font-weight: 300;
    font-size: 25px; line-height: 1; margin-top: 2px;
  }
  .row-3 { margin-top: 2px; }
  .row-3 .light-word { font-size: 68px; }
  .row-3 .bold-word { font-size: 42px; }
  .connector {
    display: flex; align-items: center; justify-content: center; gap: 10px;
    color: var(--ink); font-weight: 300; font-size: 28px; line-height: 1;
    margin-top: 2px;
  }
  .connector svg { display: block; }
  .final-line {
    color: var(--ink); font-weight: 900; font-size: 42px; line-height: 1.05;
    letter-spacing: -0.3px;
  }
</style>
</head>
<body>
  <main class="cover-wrap">
    <section class="back-cover">
      <div class="top-band"><p class="author">Author Name</p></div>
      <div class="blurb-band">
        <p class="blurb">Lorem ipsum dolor sit amet, consectetur adipiscing elit, sed do eiusmod tempor incididunt ut labore et dolore magna aliqua. Elit scelerisque mauris pellentesque pulvinar pellentesque habitant morbi tristique senectus. Vitae purus faucibus ornare suspendisse sed nisi lacus. In eu mi bibendum neque egestas congue quisque. Id faucibus nisl tincidunt eget nullam non nisi est. Aliquet nec ullamcorper sit amet risus nullam. Lacus sed turpis tincidunt id aliquet. Venenatis urna cursus eget nunc scelerisque viverra. Maecenas pharetra convallis posuere morbi leo. Tristique risus nec feugiat in fermentum posuere. Et malesuada fames ac turpis egestas. Aliquam purus sit amet luctus venenatis lectus magna.</p>
      </div>
      <div class="bottom-band"></div>
    </section>

    <section class="spine">
      <p class="author">Author Name</p>
      <p class="title"><b>Ninety</b> Truths Earned Across<br><b>Four</b> Decades of <b>Advisory Work</b></p>
    </section>

    <section class="front-cover">
      <div class="top-band"></div>
      <div class="title-band">
        <h1 class="title-block">
          <span class="title-row row-1"><span class="light-word">Ninety</span><span class="bold-word">Truths</span></span>
          <span class="subline" style="display:block">Earned Across</span>
          <span class="title-row row-3"><span class="light-word">Four</span><span class="bold-word">Decades</span></span>
          <span class="connector">
            <svg width="72" height="2" aria-hidden="true"><rect width="72" height="2" fill="var(--red)"/></svg>
            of
            <svg width="72" height="2" aria-hidden="true"><rect width="72" height="2" fill="var(--red)"/></svg>
          </span>
          <span class="final-line" style="display:block">Advisory Work</span>
        </h1>
      </div>
      <div class="bottom-band"><p class="author">Author Name</p></div>
    </section>
  </main>
</body>
</html>
```